Qorvane Management LLC Business Card

The sample logo was attached for the business Card Design for Traffic Control Company named Qorvane Management LLC. Card design needs to have the company logo and colors match the logo color. It will be nice to show some images of Traffic control signs or cones, even roads closer that math the company services

Target Market(s)

Temporary traffic control. Road closer.

Industry/Entity Type

Construction

Contact Information for Business Card

basic information, name, job title, address, email phone, website

Font styles to use
Serif
Sans Serif

Colors
F0912C
F2A743
F7CA91
FBE8D2
FDF5EE
EE7325
F08F49
F5BC92
FAE3D3
FDF4ED

```html
<!DOCTYPE html>
<html lang="en">
<head>
<meta charset="utf-8">
<title>Qorvane Management LLC – Business Card</title>
<link rel="stylesheet" href="https://fonts.googleapis.com/css2?family=Lato:wght@400;700;900&display=swap">
<style>
  :root {
    --stage: #d9d9db;
    --card: #1e1f21;
    --orange: #ee7325;
    --white: #ffffff;
    --rule: #8a8a8c;
    --sky: #b9c3d2;
    --foliage: #6f7a4a;
    --road: #5b6164;
    --cone: #f0642a;
  }
  * { box-sizing: border-box; margin: 0; padding: 0; }
  html, body { width: 1200px; height: 1108px; overflow: hidden; }
  body {
    background: var(--stage);
    font-family: "Lato", Arial, sans-serif;
    position: relative;
  }
  .card {
    position: absolute;
    top: 186px;
    width: 420px;
    height: 735px;
    background: var(--card);
    border-radius: 18px;
    overflow: hidden;
    box-shadow: 0 10px 30px rgba(0,0,0,.25);
  }
  .card--front { left: 150px; color: var(--white); text-align: center; }
  .card--back { left: 630px; }

  .brand { position: absolute; top: 150px; left: 0; right: 0; }
  .brand__mark {
    display: inline-block; width: 22px; height: 22px;
    background: var(--orange); margin-bottom: 14px;
  }
  .brand__name {
    color: var(--orange); font-weight: 900;
    font-size: 52px; letter-spacing: 3px; line-height: 1;
  }
  .brand__sub {
    color: var(--orange); font-weight: 900;
    font-size: 25px; letter-spacing: 4px; margin-top: 10px;
  }

  .person { position: absolute; top: 372px; left: 0; right: 0; }
  .person__name {
    color: var(--orange); font-weight: 700;
    font-size: 27px; letter-spacing: 1px;
  }
  .person__role { font-size: 19px; margin-top: 2px; }

  .icons {
    position: absolute; top: 432px; left: 40px; right: 40px;
    display: flex; align-items: center; gap: 8px;
  }
  .icons__rule { flex: 1; height: 1px; background: var(--rule); }
  .icons__box {
    width: 32px; height: 32px; background: var(--orange);
    border-radius: 4px; display: flex; align-items: center; justify-content: center;
  }

  .contact { position: absolute; top: 482px; left: 0; right: 0; font-size: 20px; line-height: 29px; }
  .divider { position: absolute; top: 582px; left: 40px; right: 40px; height: 1px; background: var(--rule); }
  .address { position: absolute; top: 600px; left: 0; right: 0; font-size: 20px; line-height: 29px; }

  .photo { position: absolute; border: 4px solid var(--orange); }
  .photo--signal {
    left: -4px; top: -4px; width: 318px; height: 354px;
    background: linear-gradient(180deg, var(--sky) 0%, #a8b3b8 30%, var(--foliage) 65%, #4d5533 100%);
  }
  .photo--cones {
    left: 150px; top: 300px; width: 274px; height: 439px;
    background: linear-gradient(180deg, #c9ccd0 0%, #7d6e5a 25%, var(--road) 45%, #8a4a30 75%, var(--cone) 100%);
  }
</style>
</head>
<body>
  <section class="card card--front" aria-label="Business card front">
    <div class="brand">
      <span class="brand__mark"></span>
      <div class="brand__name">QORVANE</div>
      <div class="brand__sub">MANAGEMENT LLC</div>
    </div>

    <div class="person">
      <div class="person__name">DANIEL MARLOW</div>
      <div class="person__role">Managing Director</div>
    </div>

    <div class="icons">
      <span class="icons__rule"></span>
      <span class="icons__box">
        <svg width="18" height="18" viewBox="0 0 24 24" fill="#1e1f21"><path d="M6.6 10.8a15 15 0 0 0 6.6 6.6l2.2-2.2c.3-.3.7-.4 1-.2 1.1.4 2.3.6 3.6.6.6 0 1 .4 1 1V20c0 .6-.4 1-1 1C10.6 21 3 13.4 3 4c0-.6.4-1 1-1h3.5c.6 0 1 .4 1 1 0 1.3.2 2.5.6 3.6.1.3 0 .7-.2 1z"/></svg>
      </span>
      <span class="icons__box">
        <svg width="18" height="18" viewBox="0 0 24 24" fill="none" stroke="#1e1f21" stroke-width="2"><rect x="3" y="5" width="18" height="14"/><path d="M3 5l9 8 9-8M3 19l7-7M21 19l-7-7"/></svg>
      </span>
      <span class="icons__box">
        <svg width="18" height="18" viewBox="0 0 24 24" fill="none" stroke="#1e1f21" stroke-width="2"><circle cx="12" cy="12" r="9"/><path d="M3 12h18M12 3c3 3 3 15 0 18M12 3c-3 3-3 15 0 18"/></svg>
      </span>
      <span class="icons__rule"></span>
    </div>

    <div class="contact">
      <div>044-555 018 274</div>
      <div>info@qorvane-mgmt.com</div>
      <div>www.qorvane-mgmt.com</div>
    </div>
    <div class="divider"></div>
    <div class="address">
      <div>318, Harlow Road</div>
      <div>45870, Westmere</div>
    </div>
  </section>

  <section class="card card--back" aria-label="Business card back">
    <div class="photo photo--signal" role="img" aria-label="Photo of a traffic signal on a blue pole showing red, in front of trees and sky"></div>
    <div class="photo photo--cones" role="img" aria-label="Photo of orange traffic cones lined up along a closed road"></div>
  </section>
</body>
</html>
```